Corporate Website For Tech Company

Need markup (HTML Template) + external CSS for a Corporate Website of a Tech Company (with focus on gaming). Our requirements are:
- Professional and clean look
- Usability, ease of navigation. Placeholders for navigation/pages: About Us, Services, Coming Soon
- Use of our logo in header/heading and colors and tones that blend well with it. Want to see a design with a light color background as well as one with a dark background
- Tab-based horizontal navigation preferable. Willing to consider other navigational options
- Light CSS and/or Javascript. No convoluted or over-the-top use of graphics for elements which can cause slow rendering. Use of graphics is fine but don’t overdo it
- Clean organization of page components as containers: header, body and footer

Reason: Give more time for designers that have recently accepted to submit their designs

It Company

```html
<!DOCTYPE html>
<html lang="en">
<head>
<meta charset="utf-8">
<title>Novaquill Labs</title>
<link rel="stylesheet" href="https://fonts.googleapis.com/css2?family=Open+Sans:wght@400;600;700&display=swap">
<style>
:root{
  --orange:#f0622a;
  --orange-dark:#d94a16;
  --red:#c0202a;
  --crimson:#b3151f;
  --grey-bar:#dcdcdc;
  --text:#555;
  --text-dark:#222;
  --footer:#000;
  --white:#fff;
}
*{box-sizing:border-box;margin:0;padding:0}
html,body{width:702px;height:1200px;overflow:hidden}
body{position:relative;background:var(--white);font-family:"Open Sans",Arial,sans-serif;color:var(--text)}

/* header */
.site-header{position:absolute;left:0;top:0;width:702px;height:372px;
  background:radial-gradient(ellipse at 50% 40%,#1e5fb8 0%,#133a78 35%,#0b1a33 75%,#060c18 100%);
  border-top:2px solid var(--crimson)}
.brand{position:absolute;left:0;top:16px;width:702px;text-align:center}
.brand-mark{display:block;margin:0 auto 6px;width:44px;height:44px;border-radius:50%;background:var(--orange)}
.brand-name{font-size:8px;font-weight:700;letter-spacing:1.5px;color:var(--white)}
.social-tab{position:absolute;left:269px;top:90px;width:167px;height:20px;background:#555;
  clip-path:polygon(8% 0,92% 0,100% 100%,0 100%);display:flex;justify-content:center;gap:6px;padding-top:3px}
.social-tab span{width:17px;height:15px;background:#777;border-radius:2px}
.main-nav{position:absolute;left:58px;top:106px;width:586px;height:37px;background:var(--orange);border-top:4px solid #444;display:flex;align-items:center}
.main-nav a{color:var(--white);font-size:8.5px;text-decoration:none;margin-left:26px}
.nav-search{position:absolute;right:22px;top:6px;width:117px;height:20px;border:1px solid var(--orange-dark);background:#ec5a22;font-size:7px;color:#f7a27d;padding:5px 6px}
.nav-search svg{position:absolute;right:5px;top:5px}
.hero{position:absolute;left:58px;top:143px;width:586px;height:229px;
  background:linear-gradient(120deg,#2b3040 0%,#4f7fb4 35%,#9cc7ea 55%,#3f6c9f 80%,#23293a 100%)}
.hero-arrow{position:absolute;top:100px;width:18px;height:18px;border-radius:50%;background:var(--white);display:flex;align-items:center;justify-content:center}
.hero-dots{position:absolute;left:270px;bottom:9px;display:flex;gap:4px}
.hero-dots i{width:8px;height:8px;border-radius:50%;border:1px solid var(--white)}
.hero-dots i.active{background:var(--orange);border-color:var(--orange)}

/* welcome */
.welcome-title{position:absolute;left:0;top:383px;width:702px;text-align:center;font-size:18px;font-weight:400;color:var(--crimson)}
.welcome-text{position:absolute;left:0;top:413px;width:702px;text-align:center;font-size:10.5px;line-height:17px;color:#666}
.service-card{position:absolute;top:462px;width:186px;height:113px;border:1px solid #ccc}
.service-card .art{height:94px}
.service-card .caption{height:18px;background:var(--crimson);color:var(--white);font-size:8px;padding:4px 6px;display:flex;justify-content:space-between}

/* programs */
.section-title{position:absolute;font-size:15px;font-weight:400;color:var(--crimson)}
.accordion-head{position:absolute;left:58px;width:242px;height:24px;font-size:8.5px;padding:6px 7px;color:#333;background:var(--grey-bar);display:flex;justify-content:space-between}
.accordion-head.open{background:var(--orange);color:var(--white)}
.accordion-body{position:absolute;left:64px;top:671px;width:232px;font-size:6.4px;line-height:14.4px;color:#555}
.video{position:absolute;left:321px;top:608px;width:323px;height:188px;background:linear-gradient(135deg,#1d3768,#5a86c0 50%,#1b2c52)}
.video-play{position:absolute;left:141px;top:78px;width:41px;height:28px;border-radius:6px;background:#e22;display:flex;align-items:center;justify-content:center}
.video-bar{position:absolute;left:0;bottom:0;width:100%;height:17px;background:#1a1a1a;font-size:6px;color:#ccc;padding:5px 46px}

/* news */
.tabs{position:absolute;left:60px;top:822px;width:331px;height:208px;border:1px solid #ddd}
.tab{position:absolute;top:-1px;height:33px;font-size:11px;text-align:center;padding-top:9px}
.tab.active{left:-1px;width:90px;background:var(--white);border:1px solid #ddd;border-bottom:none;color:#333}
.tab.inactive{left:89px;width:80px;top:4px;height:28px;background:#e3e3e3;color:#555}
.post{position:absolute;left:12px;width:306px;font-size:7.2px;line-height:10.8px;color:#555}
.post .thumb{float:left;width:74px;height:48px;margin:0 12px 2px 0;border:2px solid #eee}
.post h3{font-size:8px;line-height:11px;font-weight:700;color:#222}
.post .date{font-size:6.5px;line-height:9px;color:#aaa;margin-bottom:5px}
.post .more{color:var(--red)}
.post .count{position:absolute;right:0;top:0;font-size:6px;color:#aaa}
.post.second{top:122px;border-top:1px dotted #ccc;padding-top:8px}

/* about */
.about-title{position:absolute;left:458px;top:830px;font-size:11px;font-weight:400;color:#444;width:182px;border-bottom:1px solid #eee;height:24px}
.about-title::after{content:"";position:absolute;left:0;bottom:-2px;width:40px;height:2px;background:var(--red)}
.about-item{position:absolute;left:458px;width:182px;border:1px solid #ddd;font-size:8.5px;font-weight:700;padding:12px 12px;color:var(--red)}
.about-item span{position:absolute;right:10px;top:9px;font-weight:400;font-size:11px}
.about-item p{font-weight:400;color:#666;font-size:8.6px;line-height:13.6px;margin-top:12px}

/* partners */
.partners{position:absolute;left:58px;top:1052px;width:586px;height:40px;display:flex;justify-content:space-around;align-items:center}
.partner{font-size:17px;color:#555}
.partner.red{color:var(--red)}
.partner.orange{color:var(--orange)}

/* footer */
.site-footer{position:absolute;left:0;top:1114px;width:702px;height:86px;background:var(--footer);color:var(--white);text-align:center;font-size:7.8px}
.footer-links{margin-top:13px}
.footer-copy{margin-top:6px}
.footer-social{display:flex;justify-content:center;gap:5px;margin-top:8px}
.footer-social span{width:14px;height:14px;background:#3a6fbf;border-radius:2px}
.footer-social span.rss{background:var(--orange)}
</style>
</head>
<body>
<header class="site-header">
  <div class="brand"><span class="brand-mark"></span><span class="brand-name">NOVAQUILL LABS</span></div>
  <div class="social-tab"><span></span><span></span><span></span><span></span><span></span></div>
  <nav class="main-nav">
    <a>Home</a><a>About us</a><a>Services</a><a>Coming Soon</a><a>Blog</a><a>Contact us</a>
    <div class="nav-search">Search<svg width="8" height="8" viewBox="0 0 10 10"><circle cx="4" cy="4" r="3" fill="none" stroke="#222" stroke-width="1.5"/><line x1="6.5" y1="6.5" x2="9" y2="9" stroke="#222" stroke-width="1.5"/></svg></div>
  </nav>
  <div class="hero" role="img" aria-label="Laptop, phone and tablet linked by a network of people icons around a globe">
    <div class="hero-arrow" style="left:26px"><svg width="8" height="8" viewBox="0 0 8 8"><path d="M5 1 2 4l3 3" fill="none" stroke="#333" stroke-width="1.5"/></svg></div>
    <div class="hero-arrow" style="right:26px"><svg width="8" height="8" viewBox="0 0 8 8"><path d="M3 1l3 3-3 3" fill="none" stroke="#333" stroke-width="1.5"/></svg></div>
    <div class="hero-dots"><i class="active"></i><i></i><i></i></div>
  </div>
</header>

<main>
  <h1 class="welcome-title">Welcome to Novaquill Labs</h1>
  <p class="welcome-text">30+ Man years of Game Development Experience, 50+ Man Years of Mobile Development Experience.<br>PixelRank Rating: 5 out of 5 based on 5 ratings.</p>

  <div class="service-card" style="left:58px"><div class="art" role="img" aria-label="Businessman holding a phone with app icons" style="background:linear-gradient(90deg,#2a2a2a,#c9dbe6)"></div><div class="caption">Mobile Gaming Development<span>→</span></div></div>
  <div class="service-card" style="left:258px"><div class="art" role="img" aria-label="Laptop with colourful software icons" style="background:linear-gradient(180deg,#8fa9c4,#dce4ec)"></div><div class="caption">Computer Software Development<span>→</span></div></div>
  <div class="service-card" style="left:457px"><div class="art" role="img" aria-label="Phone surrounded by a cloud of app icons" style="background:linear-gradient(180deg,#b8a98c,#6e8aa0)"></div><div class="caption">Application Development<span>→</span></div></div>

  <h2 class="section-title" style="left:58px;top:603px">Devlopment Programs</h2>
  <div class="accordion-head open" style="top:638px">Innovation<span>—</span></div>
  <p class="accordion-body">Novaquill is a game development company based in India. We do not force innovation but rather shape our environment to foster it. Only in a free ecosystem where ideas flow smoothly, is true innovation born. We encourage everyone to put their best ideas forward, pick out the best.</p>
  <div class="accordion-head" style="top:742px">Quality Control<span>+</span></div>
  <div class="accordion-head" style="top:772px">Our Skills<span>+</span></div>

  <div class="video" role="img" aria-label="Video still of hand typing on a keyboard over a world map">
    <div class="video-play"><svg width="12" height="12" viewBox="0 0 12 12"><path d="M2 1l9 5-9 5z" fill="#fff"/></svg></div>
    <div class="video-bar">00:00</div>
  </div>

  <section class="tabs">
    <div class="tab active">News</div>
    <div class="tab inactive">Blog</div>
    <article class="post" style="top:46px">
      <div class="thumb" role="img" aria-label="Person in a red coat outdoors" style="background:linear-gradient(135deg,#9aa78c,#c0453e)"></div>
      <span class="count">▪ 2</span>
      <h3>Awesome Slider Post</h3><div class="date">May 30, 2013</div>
      Lorem ipsum dolor sit amet, consectetur adipisicing elit, sed do eiusmod tempor incididunt ut labore et dolore magna aliqua. Ut enim ad minim veniam, quis nostrud exercitation ullamco laboris nisi ut <span class="more">»</span>
    </article>
    <article class="post second">
      <div class="thumb" role="img" aria-label="Smiling businesswoman with colleagues" style="background:linear-gradient(135deg,#35485e,#d8c7b0)"></div>
      <span class="count" style="top:8px">▪ 0</span>
      <h3>Another Gallery post</h3><div class="date">May 1, 2013</div>
      Integer leo magna, adipiscing a ligula quis, tempor porta ipsum. Nullam quis eros congue, tempus dui eleifend, vehicula leo. Duis tincidunt justo non laoreet condimentum. Sed sit amet arcu blandit <span class="more">»</span>
    </article>
  </section>

  <h2 class="about-title">About us</h2>
  <div class="about-item" style="top:862px;height:90px">WHO WE ARE<span>—</span><p>Consectetur adipisicing elit, sed do eiusmod tempor incididunt labore et dolore magna aliqua.</p></div>
  <div class="about-item" style="top:956px;background:#f6f6f6">WHAT WE DO<span>+</span></div>
  <div class="about-item" style="top:997px;background:#f6f6f6;color:#222">WHY CHOOSE US<span>+</span></div>

  <div class="partners">
    <span class="partner red">Marlow Trust</span>
    <span class="partner red" style="font-weight:700">Keldrin Drilling</span>
    <span class="partner" style="font-size:11px;font-weight:600">hartwell-finch.com</span>
    <span class="partner orange" style="font-weight:700">jobnest</span>
  </div>
</main>

<footer class="site-footer">
  <div class="footer-links">Home \ About us \ Coming Soon \ Blog \ Contact Us</div>
  <div class="footer-copy">© 2014 Company Name All right reserved Term of Use</div>
  <div class="footer-social"><span></span><span></span><span></span><span class="rss"></span></div>
</footer>
</body>
</html>
```